label design for coffee bean packaging

Logo will be provided. Label design for package of coffee beans for a micro roasted coffee company. Need to have space to write in origin, weight with check box for 1/4, 1/2, 1lb. Need to have check boxes for Light, Medium, Dark. Creative unique label design with boarders and fun, modern design. Company name is Cedar Brook Roasting Company. See attached logo. I have source files for logo if needed for design.
Industry/Entity Type
Coffee Shop
Font styles to use
Other font styles liked:
- Montez, kautiva cyrillic, uniform bold
Colors
f78f20
faa54b
f37122
fece3e
acd036
Requirements
Must have
- logo included in the design

```html
<!DOCTYPE html>
<html lang="en">
<head>
<meta charset="utf-8">
<title>Cedar Brook Roasting Company – Coffee Bean Label</title>
<link rel="stylesheet" href="https://fonts.googleapis.com/css2?family=Maven+Pro:wght@500;700&family=Sofia&display=swap">
<style>
  :root {
    --backdrop: #4b3f31;
    --roast-brown: #5a2e12;
    --bean-orange: #f37122;
    --leaf-green: #a9cc3a;
    --paper-white: #ffffff;
    --ink-brown: #5a2e12;
  }
  html, body {
    margin: 0;
    width: 927px;
    height: 1200px;
    overflow: hidden;
    background: var(--backdrop);
  }
  .canvas {
    position: relative;
    width: 927px;
    height: 1200px;
  }
  .label {
    position: absolute;
    left: 62px;
    top: 39px;
    width: 434px;
    height: 606px;
    transform: scale(1.85);
    transform-origin: top left;
    border-radius: 20px;
    overflow: hidden;
    background: var(--roast-brown);
    font-family: "Maven Pro", Arial, sans-serif;
    color: var(--ink-brown);
  }
  .pattern {
    position: absolute;
    left: 0;
    width: 434px;
    background: linear-gradient(135deg, #5e3014 0%, #6a3717 50%, #5a2e12 100%);
  }
  .pattern--top { top: 0; height: 193px; }
  .pattern--bottom { top: 398px; height: 208px; }
  .band-rule {
    position: absolute;
    left: 0;
    width: 434px;
    height: 5px;
    background: var(--roast-brown);
  }
  .band-rule--top { top: 193px; }
  .band-rule--bottom { top: 391px; }
  .slogan-band {
    position: absolute;
    left: 0;
    top: 199px;
    width: 434px;
    height: 191px;
    background: var(--leaf-green);
  }
  .brand-seal {
    position: absolute;
    left: 92px;
    top: 51px;
    width: 246px;
    height: 246px;
    border-radius: 50%;
    background: var(--paper-white);
    border: 4px solid var(--roast-brown);
    box-sizing: border-box;
    display: flex;
    align-items: center;
    justify-content: center;
    text-align: center;
  }
  .brand-name {
    margin: 0;
    font-weight: 700;
    font-size: 29px;
    line-height: 1.15;
    color: var(--ink-brown);
  }
  .tagline {
    position: absolute;
    left: 0;
    top: 302px;
    width: 434px;
    margin: 0;
    text-align: center;
    font-family: "Sofia", cursive;
    font-size: 25px;
    line-height: 35px;
    color: var(--ink-brown);
  }
  .details-card {
    position: absolute;
    left: 14px;
    top: 455px;
    width: 403px;
    height: 138px;
    border-radius: 10px;
    background: var(--paper-white);
  }
  .field-label {
    position: absolute;
    margin: 0;
    font-weight: 500;
    font-size: 12px;
    line-height: 13px;
  }
  .write-line {
    position: absolute;
    left: 11px;
    top: 59px;
    width: 144px;
    height: 3px;
    background: var(--roast-brown);
  }
  .divider {
    position: absolute;
    top: 6px;
    width: 3px;
    height: 87px;
    background: var(--roast-brown);
  }
  .check-box {
    position: absolute;
    border: 2px solid var(--roast-brown);
    border-radius: 6px;
    box-sizing: border-box;
  }
  .weight-box { top: 36px; width: 25px; height: 35px; }
  .roast-box { left: 358px; width: 37px; height: 25px; }
  .size-label {
    position: absolute;
    top: 78px;
    margin: 0;
    font-size: 11px;
    width: 25px;
    text-align: center;
  }
  .contact {
    position: absolute;
    left: 0;
    top: 105px;
    width: 403px;
    text-align: center;
    margin: 0;
  }
  .contact-web {
    display: block;
    font-weight: 700;
    font-size: 10.5px;
    line-height: 14px;
  }
  .contact-place {
    display: block;
    font-weight: 500;
    font-size: 8px;
    line-height: 12px;
  }
  .social-square {
    position: absolute;
    top: 106px;
    width: 25px;
    height: 26px;
    border-radius: 4px;
    background: var(--roast-brown);
  }
</style>
</head>
<body>
<main class="canvas">
  <section class="label">
    <div class="pattern pattern--top" role="img" aria-label="Hand-drawn orange coffee cups, moka pots, beans and takeaway cups on brown"></div>
    <div class="band-rule band-rule--top"></div>
    <div class="slogan-band"></div>
    <div class="band-rule band-rule--bottom"></div>
    <div class="pattern pattern--bottom" role="img" aria-label="Hand-drawn orange coffee cups, moka pots, beans and takeaway cups on brown"></div>

    <div class="brand-seal">
      <p class="brand-name">Cedar Brook<br>Roasting Company</p>
    </div>

    <p class="tagline">We roast perfectly<br>for every individual taste</p>

    <div class="details-card">
      <p class="field-label" style="left:11px; top:9px;">Origin:</p>
      <div class="write-line"></div>
      <p class="field-label" style="left:11px; top:67px;">Date<br>roasted:</p>

      <div class="divider" style="left:168px;"></div>

      <p class="field-label" style="left:182px; top:9px;">Weight:</p>
      <div class="check-box weight-box" style="left:182px;"></div>
      <div class="check-box weight-box" style="left:216px;"></div>
      <div class="check-box weight-box" style="left:249px;"></div>
      <p class="size-label" style="left:182px;">1/4</p>
      <p class="size-label" style="left:216px;">1/2</p>
      <p class="size-label" style="left:249px;">1lb</p>

      <div class="divider" style="left:287px;"></div>

      <p class="field-label" style="left:303px; top:14px;">Light</p>
      <p class="field-label" style="left:303px; top:47px;">Medium</p>
      <p class="field-label" style="left:303px; top:77px;">Dark</p>
      <div class="check-box roast-box" style="top:7px;"></div>
      <div class="check-box roast-box" style="top:39px;"></div>
      <div class="check-box roast-box" style="top:70px;"></div>

      <div class="social-square" style="left:53px;"></div>
      <p class="contact">
        <span class="contact-web">www.cedarbrookroastingcompany.com</span>
        <span class="contact-place">Cedar Brook, NC 28000&nbsp;&nbsp;&nbsp;&nbsp;+1 888-555-0142</span>
      </p>
      <div class="social-square" style="left:330px;"></div>
    </div>
  </section>
</main>
</body>
</html>
```